Concrete Construction Business Card design

We are a commercial concrete construction company based in Texas. a family owned business which our trade was passed down and taught by our grandfather whom we want represented in this design. our grandfathers nick name was "pepe" so we are wanting the letter G to be symbolized in some way with a red pepe . colors should be possibly a grey color back ground , green letter g and red pepe pepper , to be left for you to decide with integrity , concrete professionalism,and mexican heritage

Target Market(s)

general contractors, architects,inverstors, and engineers

Industry/Entity Type

Concrete

Contact Information for Business Card

Herrera Concrete Construction LLC, Tobias Quintanar, 1872 Bramblewood Ln. Alderbrook, NM 88314, (555)318-2746, tqslabworkllc48@quarrymail.net

```html
<!DOCTYPE html>
<html lang="en">
<head>
<meta charset="UTF-8">
<title>Herrera Concrete Construction LLC – Business Card</title>
<link rel="stylesheet" href="https://fonts.googleapis.com/css2?family=Arimo:wght@400;700&family=Tinos:wght@700&display=swap">
<style>
  :root {
    --page-bg: #ffffff;
    --card-bg: #6d6e70;
    --card-text: #ffffff;
    --accent-green: #3bb04a;
  }
  html, body {
    margin: 0;
    padding: 0;
    width: 1200px;
    height: 1000px;
    overflow: hidden;
    background: var(--page-bg);
  }
  .canvas {
    position: relative;
    width: 1200px;
    height: 1000px;
  }
  .business-card {
    position: absolute;
    left: 283px;
    top: 313px;
    width: 635px;
    height: 373px;
    background: var(--card-bg);
    color: var(--card-text);
  }
  .brand-mark {
    position: absolute;
    left: 104px;
    top: 186px;
    width: 44px;
    height: 44px;
    border-radius: 50%;
    background: var(--accent-green);
  }
  .brand-name {
    position: absolute;
    left: 73px;
    top: 264px;
    margin: 0;
    font-family: "Tinos", "Times New Roman", serif;
    font-weight: 700;
    color: var(--card-text);
    line-height: 1;
  }
  .brand-name__family {
    display: block;
    font-size: 30px;
  }
  .brand-name__trade {
    display: block;
    font-size: 18px;
    margin-top: 3px;
  }
  .contact {
    position: absolute;
    left: 328px;
    top: 235px;
    font-family: "Arimo", Arial, sans-serif;
    color: var(--card-text);
  }
  .contact__name {
    margin: 0 0 9px;
    font-size: 14px;
    font-weight: 700;
    line-height: 1.2;
  }
  .contact__details {
    margin: 0;
    font-size: 13.5px;
    font-weight: 400;
    line-height: 18px;
    font-style: normal;
    opacity: 0.95;
  }
</style>
</head>
<body>
  <div class="canvas">
    <section class="business-card">
      <span class="brand-mark" aria-hidden="true"></span>
      <h1 class="brand-name">
        <span class="brand-name__family">Herrera</span>
        <span class="brand-name__trade">Concrete Construction LLC</span>
      </h1>
      <div class="contact">
        <p class="contact__name">Tobias Quintanar</p>
        <address class="contact__details">
          1872 Bramblewood Ln. Alderbrook, NM 88314,<br>
          (555) 318-2746,<br>
          tqslabworkllc48@quarrymail.net
        </address>
      </div>
    </section>
  </div>
</body>
</html>
```